Pitch Deck presentation

Design multiple graphics and slides that can be used in a PowerPoint presentation.
4 infographics, text templates and blank templates
Attached you will find the infographics references and a couple of styles we would like to have on the presentations
We prefer a simpler design with not too much background noise or colors(prefer to have whiter backgrounds)
The infographics in the whiteboard should be presented 1 per slide with space on the right side to write text for explanation.
4 total columns will be the equivalent to the 4 different slides with design in the presentation.
Attached you have our colors and logos.
https://files.plenvora.net/share/7kqTw2mBx9RfL4pZ
You can reach out to me with any questions at my email mtressall@haulvenix.com
Look and feel
Each slider illustrates characteristics of the customer's brand and the style your logo design should communicate.

```html
<!DOCTYPE html>
<html lang="en">
<head>
<meta charset="utf-8">
<title>Roadline Pitch Deck Overview</title>
<link href="https://fonts.googleapis.com/css2?family=Montserrat:ital,wght@0,400;0,600;0,700;0,800;1,500&display=swap" rel="stylesheet">
<style>
:root{--or:#e8501f;--dk:#333333;--mid:#777;--bg:#d9dadc;--lt:#f2f2f2}
*{box-sizing:border-box;margin:0;padding:0}
html,body{width:916px;height:1200px;overflow:hidden;background:var(--bg);font-family:Montserrat,sans-serif;color:var(--dk)}
.deck{position:relative;width:916px;height:1200px;background:linear-gradient(180deg,#e1e2e4,#d3d4d6)}
.slide{position:absolute;width:267px;height:150px;background:#fff;box-shadow:0 1px 3px rgba(0,0,0,.25);overflow:hidden}
.a{position:absolute}
.title{position:absolute;left:8px;top:8px;font-weight:700;font-size:8.5px}
.title::after{content:"";position:absolute;left:0;top:12px;width:9px;height:1.4px;background:var(--or);box-shadow:10px 0 0 -0.3px var(--dk)}
.logo{position:absolute;right:6px;top:8px;font-weight:800;font-size:5.5px;letter-spacing:.2px;color:var(--dk)}
.folio{position:absolute;left:0;right:8px;bottom:6px;border-top:.6px solid var(--or)}
.folio span{position:absolute;right:-5px;top:-2px;font-size:2.2px;color:var(--mid)}
.txt{font-size:2.2px;line-height:1.4;color:var(--mid)}
.w{color:#fff}
.or{color:var(--or)}
.st{font-weight:700;font-size:3px;color:var(--dk)}
.dot{position:absolute;border-radius:50%;background:var(--or)}
.dot::after{content:"";position:absolute;inset:28%;border:.6px solid #fff;border-radius:50%}
.darkbox{position:absolute;background:var(--dk)}
.card{position:absolute;border:1px solid var(--dk);background:#fff}
.card.o{border-color:var(--or)}
.ph{position:absolute}
</style>
</head>
<body>
<main class="deck">

<!-- 1 cover -->
<section class="slide" style="left:48px;top:45px;background:#2f2f2f">
  <div class="ph" role="img" aria-label="Photograph of a truck fleet parked beneath a bridge, black and white" style="inset:0;background:linear-gradient(100deg,#2b2b2b 30%,#555 60%,#3a3a3a)"></div>
  <div class="a" style="left:8px;top:7px;width:7px;height:7px;background:var(--or)"></div>
  <div class="a w" style="right:18px;top:12px;font-size:3px">www.<span class="or">roadline-freight</span>.com</div>
  <div class="a w" style="left:21px;top:76px;font-weight:800;font-size:15px">Business</div>
  <div class="a or" style="left:21px;top:92px;font-weight:800;font-size:19px">Marketing</div>
  <div class="a w" style="left:21px;top:116px;font-style:italic;font-weight:500;font-size:6px">Presentation</div>
  <div class="a w" style="left:21px;top:124px;width:80px;font-size:2.6px;font-style:italic;line-height:1.4">Lorem ipsum dolor sit amet, consectetuer adipiscing elit, sed diam nonum</div>
  <div class="a w" style="right:11px;top:113px;font-weight:800;font-size:16px">ROADLINE</div>
</section>

<!-- 2 agenda -->
<section class="slide" style="left:326px;top:45px">
  <div class="logo">ROADLINE</div>
  <div class="a" style="left:45px;top:67px;font-weight:800;font-size:14px">AGENDA</div>
  <div class="a" style="left:72px;top:85px;width:20px;height:1.4px;background:var(--or)"></div>
  <div class="a" style="left:119px;top:32px;width:110px">
    <div style="font-size:4.6px;font-weight:600"><span class="or">1.</span> Lorem ipsum</div>
    <div class="txt" style="padding-left:6px">Lorem ipsum dolor sit amet, consectetuer adipiscing elit, sed diam nonummy nibh euismod tincid</div>
    <div style="font-size:4.6px;font-weight:600;margin-top:11px"><span class="or">2.</span> Lorem ipsum</div>
    <div class="txt" style="padding-left:6px">Lorem ipsum dolor sit amet, consectetuer adipiscing elit, sed diam nonummy nibh euismod tincid</div>
    <div style="font-size:4.6px;font-weight:600;margin-top:11px"><span class="or">3.</span> Lorem ipsum</div>
    <div class="txt" style="padding-left:6px">Lorem ipsum dolor sit amet, consectetuer adipiscing elit, sed diam nonummy nibh euismod tincid</div>
    <div style="font-size:4.6px;font-weight:600;margin-top:11px"><span class="or">4.</span> Lorem ipsum</div>
    <div class="txt" style="padding-left:6px">Lorem ipsum dolor sit amet, consectetuer adipiscing elit, sed diam nonummy nibh euismod tincid</div>
  </div>
  <div class="folio"><span>2</span></div>
</section>

<!-- 3 list + dark panel -->
<section class="slide" style="left:604px;top:45px">
  <div class="title">Text Added Here</div><div class="logo">ROADLINE</div>
  <div class="a" style="left:33px;top:36px;width:95px">
    <div class="st"><span style="color:var(--dk)">01.</span> <span class="or">Aliquam Erat Volutpat</span></div>
    <div class="txt" style="padding-left:7px">Lorem ipsum dolor sit amet, consectetuer adipiscing elit, sed diam nonummy nibh euismod</div>
    <div class="st" style="margin-top:10px">02. <span class="or">Consectetuer Adipiscing Elit</span></div>
    <div class="txt" style="padding-left:7px">Lorem ipsum dolor sit amet, consectetuer adipiscing elit, sed diam nonummy nibh euismod tincidunt</div>
    <div class="st" style="margin-top:10px">03. <span class="or">Duis Autem Vel Eum</span></div>
    <div class="txt" style="padding-left:7px">Lorem ipsum dolor sit amet, consectetuer adipiscing elit, sed diam nonummy nibh euismod tincidunt</div>
    <div class="st" style="margin-top:10px">04. <span class="or">Aliquam Erat Volutpat</span></div>
    <div class="txt" style="padding-left:7px">Lorem ipsum dolor sit amet, consectetuer adipiscing elit, sed diam nonummy nibh euismod tincidunt</div>
  </div>
  <div class="darkbox" style="left:148px;top:35px;width:86px;height:89px"></div>
  <div class="dot" style="left:139px;top:42px;width:20px;height:20px;border:1.5px solid #fff"></div>
  <div class="dot" style="left:139px;top:71px;width:20px;height:20px;border:1.5px solid #fff"></div>
  <div class="dot" style="left:139px;top:100px;width:20px;height:20px;border:1.5px solid #fff"></div>
  <div class="a w" style="left:165px;top:44px;width:64px"><div style="font-size:4px;font-weight:600">Lorem ipsum</div><div class="txt w">ipsum dolor sit amet, cons ectetuer adipiscing elit, sed diam nonummy nibh euismod tincidunt</div></div>
  <div class="a w" style="left:165px;top:73px;width:64px"><div style="font-size:4px;font-weight:600">Lorem ipsum</div><div class="txt w">ipsum dolor sit amet, cons ectetuer adipiscing elit, sed diam nonummy nibh euismod tincidunt</div></div>
  <div class="a w" style="left:165px;top:102px;width:64px"><div style="font-size:4px;font-weight:600">Lorem ipsum</div><div class="txt w">ipsum dolor sit amet, cons ectetuer adipiscing elit, sed diam nonummy</div></div>
  <div class="folio"><span>3</span></div>
</section>

<!-- 4 hub -->
<section class="slide" style="left:48px;top:205px">
  <div class="title">Text Added Here</div><div class="logo">ROADLINE</div>
  <svg class="a" style="left:0;top:0" width="267" height="150" viewBox="0 0 267 150">
    <circle cx="58" cy="77" r="29" fill="#fff" stroke="var(--dk)" stroke-width="4"/>
    <circle cx="58" cy="77" r="24.5" fill="none" stroke="var(--or)" stroke-width=".8"/>
    <path d="M92 77 L110 77 M84 63 L102 43 L125 43 M84 91 L102 111 L125 111 M110 77 L125 77" stroke="var(--dk)" stroke-width=".6" fill="none"/>
  </svg>
  <div class="a" style="left:36px;top:73px;font-weight:800;font-size:7px">ROADLINE</div>
  <div class="dot" style="left:130px;top:36px;width:14px;height:14px"></div>
  <div class="dot" style="left:130px;top:70px;width:14px;height:14px"></div>
  <div class="dot" style="left:130px;top:104px;width:14px;height:14px"></div>
  <div class="a" style="left:157px;top:33px;width:85px"><div class="st" style="font-size:3.4px">Project name</div><div class="txt">Lorem ipsum dolor sit amet, nec an dictas equidem appellantur, ut has commune accommodare. Mea illum, ludus solet idpro.</div></div>
  <div class="a" style="left:157px;top:67px;width:85px"><div class="st" style="font-size:3.4px">Project name</div><div class="txt">Lorem ipsum dolor sit amet, nec an dictas equidem appellantur, ut has commune accommodare. Mea illum, ludus solet idpro.</div></div>
  <div class="a" style="left:157px;top:102px;width:85px"><div class="st" style="font-size:3.4px">Project name</div><div class="txt">Lorem ipsum dolor sit amet, nec an dictas equidem appellantur, ut has commune accommodare. Mea illum, ludus solet idpro.</div></div>
  <div class="folio"><span>4</span></div>
</section>

<!-- 5 idea promotion growth -->
<section class="slide" style="left:326px;top:205px">
  <div class="title">Text Added Here</div><div class="logo">ROADLINE</div>
  <div class="ph" role="img" aria-label="Faint world map backdrop" style="left:40px;top:30px;width:190px;height:85px;background:radial-gradient(ellipse,#f1f1f1 40%,#fff 75%)"></div>
  <svg class="a" style="left:0;top:0" width="267" height="150" viewBox="0 0 267 150">
    <g fill="none" stroke="var(--dk)" stroke-width="1.4">
      <rect x="50" y="37" width="42" height="62" rx="3"/><rect x="112" y="37" width="42" height="62" rx="3"/><rect x="174" y="37" width="42" height="62" rx="3"/>
    </g>
    <g fill="#fff" stroke="none"><rect x="90" y="50" width="4" height="40"/><rect x="152" y="50" width="4" height="40"/><rect x="110" y="50" width="4" height="40"/><rect x="172" y="50" width="4" height="40"/></g>
    <path d="M92 55 L112 90 M154 55 L174 90" stroke="var(--dk)" stroke-width="1.4"/>
    <path d="M92 52 L92 57 M112 88 L112 92 M154 52 L154 57 M174 88 L174 92" stroke="var(--dk)" stroke-width="1.4"/>
    <circle cx="71" cy="53" r="3" fill="none" stroke="var(--or)" stroke-width=".8"/>
    <rect x="130" y="51" width="7" height="5" fill="none" stroke="var(--or)" stroke-width=".8"/>
    <path d="M192 56 L196 52 L199 55 L202 50" stroke="var(--or)" stroke-width=".8" fill="none"/>
  </svg>
  <div class="a or" style="left:50px;top:59px;width:42px;text-align:center;font-size:3.2px;font-weight:700">IDEA</div>
  <div class="a or" style="left:112px;top:59px;width:42px;text-align:center;font-size:3.2px;font-weight:700">PROMOTION</div>
  <div class="a or" style="left:174px;top:59px;width:42px;text-align:center;font-size:3.2px;font-weight:700">GROWTH</div>
  <div class="a txt" style="left:55px;top:64px;width:32px;text-align:center;font-size:1.8px">Lorem ipsum dolor sit amet, consectetuer adipiscing elit, sed diam nonummy nibh euismod tincidunt ut laoreet dolore magna aliquam erat volutpat.</div>
  <div class="a txt" style="left:117px;top:64px;width:32px;text-align:center;font-size:1.8px">Lorem ipsum dolor sit amet, consectetuer adipiscing elit, sed diam nonummy nibh euismod tincidunt ut laoreet dolore magna aliquam erat volutpat.</div>
  <div class="a txt" style="left:179px;top:64px;width:32px;text-align:center;font-size:1.8px">Lorem ipsum dolor sit amet, consectetuer adipiscing elit, sed diam nonummy nibh euismod tincidunt ut laoreet dolore magna aliquam erat volutpat.</div>
  <div class="a txt" style="left:30px;top:116px;width:207px;text-align:center;color:#444">Lorem ipsum dolor sit amet, consectetuer adipiscing elit, sed diam nonummy nibh euismod tincidunt ut laoreet dolore magna aliquam erat volutpat. Ut wisi enim ad minim veniam, quis nostrud exerci tation ullamcorper suscipit lobortis nisl ut aliquip ex ea commodo consequat.</div>
  <div class="folio"><span>5</span></div>
</section>

<!-- 6 photo + cards -->
<section class="slide" style="left:604px;top:205px">
  <div class="logo">ROADLINE</div>
  <div class="a" style="left:14px;top:12px;font-weight:700;font-size:8.5px;line-height:1.35">Lorem Ipsum<br>Dolor Sit<br>Ametkeeper.</div>
  <div class="a" style="left:14px;top:50px;width:10px;height:1.4px;background:var(--or)"></div>
  <div class="a txt" style="left:14px;top:57px;width:68px;text-align:justify">Lorem ipsum dolor sit amet, consectetuer adipiscing elit, sed diam nonummy nibh euismod tincidunt ut laoreet dolore magna aliquam erat volutpat.<br><br>Ut wisi enim ad minim veniam, quis nostrud exerci tation ullamcorper suscipit lobortis nisl ut aliquip ex ea commodo consequat. Duis autem vel eum iriure dolor in hendrerit in vulputate velit esse molestie consequat.<br><br>vel illum dolore eu feugiat nulla facilisis at vero eros et accumsan et iusto odio dignissim qui blandit praesent</div>
  <div class="ph" role="img" aria-label="Black and white photograph of trucks on a highway" style="left:92px;top:26px;width:175px;height:68px;background:linear-gradient(90deg,#5a5a5a,#bdbdbd 60%,#8a8a8a)"></div>
  <div class="a" style="left:116px;top:75px;width:47px;height:62px;background:#fff;box-shadow:0 .5px 2px rgba(0,0,0,.3)"><div style="background:var(--or);height:16px;color:#fff;font-weight:700;font-size:7px;text-align:center;line-height:16px">Text Here</div><div class="txt" style="padding:2px 4px;font-size:1.9px">Lorem ipsum dolor sit amet, consectetuer adipiscing elit, sed diam nonummy nibh euismod tincidunt ut laoreet dolore magna aliquam erat volutpat.<br><br>Ut wisi enim ad minim veniam, quis nostrud exerci tation ullamcorper suscipit lobortis nisl ut aliquip ex ea commodo conse</div></div>
  <div class="a" style="left:180px;top:75px;width:47px;height:62px;background:#fff;box-shadow:0 .5px 2px rgba(0,0,0,.3)"><div style="background:var(--or);height:16px;color:#fff;font-weight:700;font-size:7px;text-align:center;line-height:16px">Text Here</div><div class="txt" style="padding:2px 4px;font-size:1.9px">Lorem ipsum dolor sit amet, consectetuer adipiscing elit, sed diam nonummy nibh euismod tincidunt ut laoreet dolore magna aliquam erat volutpat.<br><br>Ut wisi enim ad minim veniam, quis nostrud exerci tation ullamcorper suscipit lobortis nisl ut aliquip ex ea commodo conse</div></div>
  <div class="folio"><span>6</span></div>
</section>

<!-- 7 market chart -->
<section class="slide" style="left:48px;top:366px">
  <div class="logo">ROADLINE</div>
  <div class="a" style="left:14px;top:17px;font-weight:700;font-size:8.5px;line-height:1.3">Market<br>Opportunities.</div>
  <div class="a" style="left:29px;top:44px;width:10px;height:1.4px;background:var(--or)"></div>
  <div class="darkbox" style="left:0;top:55px;width:92px;height:74px"></div>
  <div class="a txt w" style="left:11px;top:60px;width:72px;font-size:3.6px;line-height:1.3">Lorem ipsum dolor sit amet, consectetuer adipiscing elit, sed diam nonummy nibh euismod tincidunt ut laoreet dolore magna aliquam erat volutpat. Ut wisi enim ad minim veniam, quis nostrud exerci tation ullamcorper suscipit lobortis nisl ut aliquip ex ea commodo consequat. Duis autem vel eum iriure dolor in hendrerit</div>
  <div class="a" style="left:110px;top:23px;font-size:3.8px;color:#444">CONSECTETUER ADIPISCING</div>
  <svg class="a" style="left:100px;top:33px" width="160" height="70" viewBox="0 0 160 70">
    <g stroke="#999" stroke-width=".3"><line x1="10" y1="2" x2="150" y2="2"/><line x1="10" y1="12.3" x2="150" y2="12.3"/><line x1="10" y1="22.6" x2="150" y2="22.6"/><line x1="10" y1="33" x2="150" y2="33"/><line x1="10" y1="43.3" x2="150" y2="43.3"/><line x1="10" y1="53.6" x2="150" y2="53.6"/><line x1="10" y1="64" x2="150" y2="64" stroke="#333" stroke-width=".5"/><line x1="10" y1="2" x2="10" y2="64"/><line x1="150" y1="2" x2="150" y2="64"/></g>
    <g font-size="4" fill="#333" font-family="Montserrat,sans-serif" text-anchor="end"><text x="7" y="3.5">60</text><text x="7" y="14">50</text><text x="7" y="24">40</text><text x="7" y="34.5">30</text><text x="7" y="45">20</text><text x="7" y="55">10</text><text x="7" y="65.5">0</text></g>
    <rect x="20" y="8.2" width="15" height="55.8" fill="var(--or)"/>
    <rect x="48" y="32" width="15" height="32" fill="var(--dk)"/>
    <rect x="77" y="16.5" width="15" height="47.5" fill="var(--or)"/>
    <rect x="105" y="36" width="15" height="28" fill="var(--dk)"/>
    <g font-size="4" fill="#333" font-family="Montserrat,sans-serif" text-anchor="middle"><text x="27.5" y="70">JAN</text><text x="55.5" y="70">FEB</text><text x="84.5" y="70">MAR</text><text x="112.5" y="70">APR</text></g>
  </svg>
  <div class="dot" style="left:108px;top:116px;width:4px;height:4px"></div>
  <div class="a st" style="left:115px;top:115px;font-size:4px">Lorem Ipsum</div>
  <div class="a txt" style="left:115px;top:121px;width:60px">Lorem ipsum dolor sit amet, consectetuer adipiscing elit, sed diam nonummy nibh euismod tincidunt ut laoreet</div>
  <div class="dot" style="left:182px;top:116px;width:4px;height:4px"></div>
  <div class="a st" style="left:189px;top:115px;font-size:4px">Lorem Ipsum</div>
  <div class="a txt" style="left:189px;top:121px;width:60px">Lorem ipsum dolor sit amet, consectetuer adipiscing elit, sed diam nonummy nibh euismod tincidunt ut laoreet</div>
  <div class="folio"><span>7</span></div>
</section>

<!-- 8 four cards -->
<section class="slide" style="left:326px;top:366px">
  <div class="title">Text Added Here</div><div class="logo">ROADLINE</div>
  <div class="ph" role="img" aria-label="Faint world map backdrop" style="left:35px;top:35px;width:200px;height:85px;background:radial-gradient(ellipse,#f2f2f2 40%,#fff 75%)"></div>
  <div class="card" style="left:38px;top:43px;width:42px;height:59px"></div>
  <div class="card o" style="left:89px;top:43px;width:42px;height:59px"></div>
  <div class="card" style="left:140px;top:43px;width:42px;height:59px"></div>
  <div class="card o" style="left:191px;top:43px;width:42px;height:59px"></div>
  <div class="dot" style="left:53px;top:37px;width:12px;height:12px;border:1px solid var(--dk)"></div>
  <div class="dot" style="left:104px;top:37px;width:12px;height:12px;background:var(--dk);border:1px solid var(--or)"></div>
  <div class="dot" style="left:155px;top:37px;width:12px;height:12px;border:1px solid var(--dk)"></div>
  <div class="dot" style="left:206px;top:37px;width:12px;height:12px;background:var(--dk);border:1px solid var(--or)"></div>
  <div class="a" style="left:43px;top:56px;width:33px"><div class="st" style="font-size:3.4px">Lorem ipsum</div><div class="txt" style="font-size:1.8px">ipsum dolor sit amet, cons ectetuer adipiscing elit, sed diam nonummy nibh euismod tincid ut laoreet<br><br>ipsum dolor sit amet, cons ectetuer adipiscing elit, sed diam nonummy nibh euismod tincidunt ut laoreet ipsum dolor sit amet, cons ectetuer</div></div>
  <div class="a" style="left:94px;top:56px;width:33px"><div class="st or" style="font-size:3.4px">Lorem ipsum</div><div class="txt" style="font-size:1.8px">ipsum dolor sit amet, cons ectetuer adipiscing elit, sed diam nonummy nibh euismod tincid ut laoreet<br><br>ipsum dolor sit amet, cons ectetuer adipiscing elit, sed diam nonummy nibh euismod tincidunt ut laoreet ipsum dolor sit amet, cons ectetuer</div></div>
  <div class="a" style="left:145px;top:56px;width:33px"><div class="st" style="font-size:3.4px">Lorem ipsum</div><div class="txt" style="font-size:1.8px">ipsum dolor sit amet, cons ectetuer adipiscing elit, sed diam nonummy nibh euismod tincid ut laoreet<br><br>ipsum dolor sit amet, cons ectetuer adipiscing elit, sed diam nonummy nibh euismod tincidunt ut laoreet ipsum dolor sit amet, cons ectetuer</div></div>
  <div class="a" style="left:196px;top:56px;width:33px"><div class="st or" style="font-size:3.4px">Lorem ipsum</div><div class="txt" style="font-size:1.8px">ipsum dolor sit amet, cons ectetuer adipiscing elit, sed diam nonummy nibh euismod tincid ut laoreet<br><br>ipsum dolor sit amet, cons ectetuer adipiscing elit, sed diam nonummy nibh euismod tincidunt ut laoreet ipsum dolor sit amet, cons ectetuer</div></div>
  <div class="a or" style="left:39px;top:108px;font-weight:700;font-size:8px">+ 35k</div>
  <div class="a txt" style="left:39px;top:120px;width:150px;font-size:1.8px">Lorem ipsum dolor sit amet, consectetuer adipiscing elit, sed diam nonummy nibh euismod tincidunt ut laoreet dolore magna aliquam erat volutpat. Ut wisi enim ad minim veniam, quis nostrud exerci tation ullamcorper.</div>
  <div class="folio"><span>8</span></div>
</section>

<!-- 9 text grid -->
<section class="slide" style="left:604px;top:366px">
  <div class="title">Text Added Here</div><div class="logo">ROADLINE</div>
  <div class="a" style="left:16px;top:35px;width:72px"><div class="st or">1. Text Added Here</div><div class="txt" style="text-align:justify">Lorem ipsum dolor sit amet, cons ectetuer adipiscing elit, sed diam nonummy nibh euismod tincidunt ut laoreet dolore magna aliquam erat volutpat. Ut wisi enim ad minim veniam, quis nostrud exerci tation ullamcorper suscipit lobortis nisl ut aliquip ex ea commodo consequat.<br><br>Lorem ipsum dolor sit amet, cons ectetuer adipiscing elit, sed diam nonummy nibh euismod tincidunt ut</div></div>
  <div class="a" style="left:98px;top:35px;width:72px"><div class="st">1. Text Added Here</div><div class="txt" style="text-align:justify">Lorem ipsum dolor sit amet, cons ectetuer adipiscing elit, sed diam nonummy nibh euismod tincidunt ut laoreet dolore magna aliquam erat volutpat. Ut wisi enim ad minim veniam, quis nostrud exerci tation ullamcorper suscipit lobortis nisl ut aliquip ex ea commodo consequat.<br><br>Lorem ipsum dolor sit amet, cons ectetuer adipiscing elit, sed diam nonummy nibh euismod tincidunt ut</div></div>
  <div class="a" style="left:178px;top:35px;width:72px"><div class="st or">1. Text Added Here</div><div class="txt" style="text-align:justify">Lorem ipsum dolor sit amet, cons ectetuer adipiscing elit, sed diam nonummy nibh euismod tincidunt ut laoreet dolore magna aliquam erat volutpat.<br><br>Lorem ipsum dolor sit amet, cons ectetuer adipiscing elit, sed diam nonummy nibh euismod tincidunt ut laoreet dolore magna aliquam erat volutpat. Ut wisi enim ad minim veniam, quis nostrud exerci tation ullamcorper suscipit lobortis nisl ut aliquip</div></div>
  <div class="a" style="left:16px;top:85px;width:72px"><div class="st">1. Text Added Here</div><div class="txt" style="text-align:justify">Lorem ipsum dolor sit amet, cons ectetuer adipiscing elit, sed diam nonummy nibh euismod tincidunt ut laoreet dolore magna aliquam erat volutpat. Ut wisi enim ad minim veniam, quis nostrud exerci tation ullamcorper.<br><br>Lorem ipsum dolor sit amet, cons ectetuer adipiscing elit, sed diam nonummy nibh euismod tincidunt ut laoreet dolore magna aliquam erat volutpat.</div></div>
  <div class="a" style="left:98px;top:85px;width:72px"><div class="st or">1. Text Added Here</div><div class="txt" style="text-align:justify">Lorem ipsum dolor sit amet, cons ectetuer adipiscing elit, sed diam nonummy nibh euismod tincidunt ut laoreet dolore magna aliquam erat volutpat. Ut wisi enim ad minim veniam, quis nostrud exerci tation ullamcorper.<br><br>Lorem ipsum dolor sit amet, cons ectetuer adipiscing elit, sed diam nonummy nibh euismod tincidunt ut laoreet dolore magna aliquam erat volutpat.</div></div>
  <div class="a" style="left:178px;top:85px;width:72px"><div class="st">1. Text Added Here</div><div class="txt" style="text-align:justify">Lorem ipsum dolor sit amet, cons ectetuer adipiscing elit, sed diam nonummy nibh euismod tincidunt ut laoreet dolore magna aliquam erat volutpat. Ut wisi enim ad minim veniam, quis nostrud exerci tation ullamcorper.<br><br>Lorem ipsum dolor sit amet, cons ectetuer adipiscing elit, sed diam nonummy nibh euismod tincidunt ut laoreet dolore magna aliquam erat volutpat.</div></div>
  <div class="folio"><span>9</span></div>
</section>

<!-- 10 CBT technology -->
<section class="slide" style="left:48px;top:528px">
  <div class="title">CBT TECHNOLOGY</div><div class="logo">ROADLINE</div>
  <svg class="a" style="left:0;top:0" width="267" height="150" viewBox="0 0 267 150" font-family="Montserrat,sans-serif">
    <line x1="36" y1="48" x2="58" y2="48" stroke="var(--dk)" stroke-width=".5"/><path d="M58 46.8 L60 48 L58 49.2Z" fill="var(--dk)"/>
    <rect x="86" y="33" width="13" height="8" fill="var(--dk)"/>
    <path d="M92 48 L92 58" stroke="var(--dk)" stroke-width=".5"/>
    <circle cx="93" cy="84" r="17" fill="none" stroke="var(--dk)" stroke-width="1.4" stroke-dasharray="20 6"/>
    <circle cx="93" cy="84" r="12" fill="var(--or)" stroke="#fff" stroke-width="1"/>
    <circle cx="93" cy="84" r="13.3" fill="none" stroke="var(--dk)" stroke-width=".8"/>
    <g fill="var(--or)"><circle cx="71" cy="84" r="2.6"/><circle cx="115" cy="84" r="2.6"/><circle cx="80" cy="101" r="2.6"/><circle cx="106" cy="101" r="2.6"/><circle cx="93" cy="62" r="2.6"/></g>
    <text x="93" y="86" fill="#fff" font-size="7" font-weight="700" text-anchor="middle">CBT</text>
    <text x="93" y="89.5" fill="#fff" font-size="1.6" text-anchor="middle">TECHNOLOGY</text>
    <g fill="none" stroke="var(--dk)" stroke-width=".8"><path d="M237 38 C250 40 250 58 237 60"/><path d="M237 60 C250 62 250 80 237 82"/><path d="M237 82 C250 84 250 102 237 104"/><path d="M237 104 C250 106 250 124 237 126"/><path d="M185 68 C178 70 176 76 180 80"/></g>
  </svg>
  <div class="a" style="left:18px;top:34px;width:54px;text-align:center;font-weight:600;font-size:3.8px;line-height:1.3">BUDGETING<br>SUSTAINABLE RATE</div>
  <div class="a" style="left:105px;top:35px;font-weight:700;font-size:4px">X &nbsp;3 PER WEEK</div>
  <div class="a" style="left:96px;top:62px;font-weight:700;font-size:3.4px">ESTABLISHED RATE</div>
  <div class="a" style="left:190px;top:36px;font-weight:700;font-size:3.6px">TRADITIONAL TMS</div>
  <div class="a or" style="left:163px;top:48px;font-weight:700;font-size:3.6px">90% + ACCEPTANCE</div>
  <div class="a or" style="left:216px;top:66px;font-size:2.6px">PRIMARY</div>
  <div class="a or" style="left:210px;top:81px;font-size:2.6px">SECENDARY</div>
  <div class="a or" style="left:213px;top:98px;font-size:2.6px">THIRTIARY</div>
  <div class="a" style="left:174px;top:80px;font-weight:700;font-size:2.8px;text-align:center;line-height:1.3">BROKERAGE<br>POOL</div>
  <div class="a" style="left:208px;top:114px;font-weight:700;font-size:2.8px;text-align:center;line-height:1.3">BROKERAGE<br>POOL</div>
  <div class="a or" style="left:13px;top:74px;font-weight:700;font-size:3.6px;line-height:1.25">BUDGETING<br>RELATIONSHIPS</div>
  <div class="a" style="left:15px;top:88px;font-size:3.5px;line-height:1.75">• Competing<br>• Incentivizing<br>• Direct Carrier<br>• Transparency</div>
  <div class="a" style="left:65px;top:121px;font-weight:700;font-size:3.8px">CARRIER ROTATION</div>
  <div class="folio"><span>10</span></div>
</section>

<!-- 11 spot market -->
<section class="slide" style="left:326px;top:528px">
  <div class="title">SPOT MARKET</div><div class="logo">ROADLINE</div>
  <div class="a" style="left:128px;top:30px;height:100px;border-left:.5px dashed #bbb"></div>
  <div class="a" style="left:19px;top:33px;font-weight:700;font-size:5px">BROKERAGE MANAGED</div>
  <div class="a" style="left:144px;top:33px;font-weight:700;font-size:5px">CBT SHIPPER MANAGED</div>
  <div class="a or" style="left:20px;top:46px;font-weight:600;font-size:3.8px">SHIPER</div>
  <div class="a" style="left:29px;top:52px;width:.6px;height:6px;background:var(--dk)"></div>
  <div class="a" style="left:25px;top:60px;width:9px;height:5px;background:var(--dk)"></div>
  <div class="a or" style="left:38px;top:60px;font-weight:600;font-size:3.8px">1 SHIPMENT</div>
  <div class="a" style="left:29px;top:67px;width:.6px;height:6px;background:var(--dk)"></div>
  <div class="a or" style="left:19px;top:74px;font-weight:700;font-size:3.8px">BROKERS</div>
  <svg class="a" style="left:17px;top:78px" width="30" height="8" viewBox="0 0 30 8"><g fill="var(--dk)"><circle cx="3" cy="2" r="1.4"/><circle cx="9" cy="2" r="1.4"/><circle cx="15" cy="2" r="1.4"/><circle cx="21" cy="2" r="1.4"/><circle cx="27" cy="2" r="1.4"/><rect x="1" y="4" width="28" height="3" rx="1"/></g></svg>
  <svg class="a" style="left:23px;top:88px" width="16" height="10" viewBox="0 0 16 10"><rect x="0" y="1" width="9" height="6" fill="var(--dk)"/><path d="M9 3 H13 L15 5.5 V7 H9Z" fill="var(--dk)"/><circle cx="3" cy="8.3" r="1.5" fill="var(--dk)"/><circle cx="12" cy="8.3" r="1.5" fill="var(--dk)"/></svg>
  <div class="a" style="left:21px;top:100px;font-weight:600;font-size:2.8px">CARRIERS</div>
  <div class="a" style="left:51px;top:80px;font-weight:600;font-size:2.8px">DEMAND</div>
  <div class="a" style="left:51px;top:94px;font-weight:600;font-size:2.8px">SUPPLY</div>
  <svg class="a" style="left:84px;top:76px" width="20" height="22" viewBox="0 0 20 22"><g fill="var(--dk)"><rect x="1" y="14" width="3" height="8"/><rect x="6" y="10" width="3" height="12"/><rect x="11" y="8" width="3" height="14"/><rect x="16" y="5" width="3" height="17"/></g><path d="M1 11 L8 5 L11 8 L18 1" stroke="var(--or)" stroke-width="1.2" fill="none"/></svg>
  <div class="a" style="left:88px;top:100px;font-weight:600;font-size:2.8px">PRICE</div>
  <div class="a or" style="left:145px;top:51px;font-weight:600;font-size:5px">SHIPER</div>
  <div class="a" style="left:157px;top:59px;width:.6px;height:8px;background:var(--dk)"></div>
  <div class="a" style="left:150px;top:69px;width:16px;height:8px;background:var(--dk)"></div>
  <div class="a" style="left:177px;top:71px;font-weight:600;font-size:4px">DEMAND</div>
  <svg class="a" style="left:150px;top:84px" width="18" height="11" viewBox="0 0 16 10"><rect x="0" y="1" width="9" height="6" fill="var(--dk)"/><path d="M9 3 H13 L15 5.5 V7 H9Z" fill="var(--dk)"/><circle cx="3" cy="8.3" r="1.5" fill="var(--dk)"/><circle cx="12" cy="8.3" r="1.5" fill="var(--dk)"/></svg>
  <div class="a" style="left:177px;top:90px;font-weight:600;font-size:4px">SUPPLY</div>
  <div class="a" style="left:147px;top:102px;font-weight:600;font-size:4px">CARRIERS</div>
  <svg class="a" style="left:217px;top:78px" width="28" height="24" viewBox="0 0 28 24"><g fill="var(--dk)"><rect x="1" y="6" width="4" height="18"/><rect x="7" y="10" width="4" height="14"/><rect x="13" y="13" width="4" height="11"/><rect x="19" y="16" width="4" height="8"/></g><path d="M1 1 L9 6 L12 3 L26 14" stroke="var(--or)" stroke-width="1.6" fill="none"/></svg>
  <div class="a" style="left:222px;top:104px;font-weight:600;font-size:4px">PRICE</div>
  <div class="folio"><span>11</span></div>
</section>

<!-- 12 list + dark panel variant -->
<section class="slide" style="left:604px;top:528px">
  <div class="title">Text Added Here</div><div class="logo">ROADLINE</div>
  <div class="a" style="left:26px;top:36px;width:98px">
    <div class="st">01. Aliquam Erat Volutpat</div><div class="txt" style="padding-left:7px">Lorem ipsum dolor sit amet, consectetuer adipiscing elit, sed diam nonummy nibh euismod</div>
    <div class="st" style="margin-top:10px">02. Consectetuer Adipiscing Elit</div><div class="txt" style="padding-left:7px">Lorem ipsum dolor sit amet, consectetuer adipiscing elit, sed diam nonummy nibh euismod tincidunt</div>
    <div class="st" style="margin-top:10px">03. Duis Autem Vel Eum</div><div class="txt" style="padding-left:7px">Lorem ipsum dolor sit amet, consectetuer adipiscing elit, sed diam nonummy nibh euismod tincidunt</div>
    <div class="st" style="margin-top:10px">04. Aliquam Erat Volutpat</div><div class="txt" style="padding-left:7px">Lorem ipsum dolor sit amet, consectetuer adipiscing elit, sed diam nonummy nibh euismod tincidunt</div>
  </div>
  <div class="darkbox" style="left:141px;top:33px;width:97px;height:95px"></div>
  <div class="dot" style="left:134px;top:39px;width:18px;height:18px;border:2px solid #fff"></div>
  <div class="dot" style="left:134px;top:67px;width:18px;height:18px;border:2px solid #fff"></div>
  <div class="dot" style="left:134px;top:96px;width:18px;height:18px;border:2px solid #fff"></div>
  <div class="a" style="left:158px;top:42px;width:74px"><div class="or" style="font-size:4px;font-weight:600">Lorem ipsum</div><div class="txt w">ipsum dolor sit amet, cons ectetuer adipiscing elit, sed diam nonummy nibh euismod tincidunt</div></div>
  <div class="a" style="left:158px;top:70px;width:74px"><div class="or" style="font-size:4px;font-weight:600">Lorem ipsum</div><div class="txt w">ipsum dolor sit amet, cons ectetuer adipiscing elit, sed diam nonummy nibh euismod tincidunt</div></div>
  <div class="a" style="left:158px;top:99px;width:74px"><div class="or" style="font-size:4px;font-weight:600">Lorem ipsum</div><div class="txt w">ipsum dolor sit amet, cons ectetuer adipiscing elit, sed diam nonummy</div></div>
  <div class="folio"><span>12</span></div>
</section>

<!-- 13 timeline -->
<section class="slide" style="left:48px;top:688px">
  <div class="title">Text Added Here</div><div class="logo">ROADLINE</div>
  <svg class="a" style="left:0;top:0" width="267" height="150" viewBox="0 0 267 150" font-family="Montserrat,sans-serif">
    <g><path d="M25 84 L30 76 L66 76 L70 84Z" fill="var(--or)"/><path d="M68 76 L112 76 L107 84 L73 84Z" fill="var(--dk)"/><path d="M110 84 L115 76 L152 76 L156 84Z" fill="var(--or)"/><path d="M154 76 L198 76 L193 84 L159 84Z" fill="var(--dk)"/><path d="M196 84 L201 76 L238 76 L242 84Z" fill="var(--or)"/></g>
    <g fill="#fff" font-size="3.6" font-weight="700" text-anchor="middle"><text x="47" y="81.6">1990</text><text x="90" y="81.6">2001</text><text x="133" y="81.6">2007</text><text x="176" y="81.6">2012</text><text x="219" y="81.6">2020</text></g>
    <g stroke="var(--or)" stroke-width=".6"><line x1="47" y1="64" x2="47" y2="75"/><line x1="133" y1="64" x2="133" y2="75"/><line x1="219" y1="64" x2="219" y2="75"/></g>
    <g fill="var(--or)"><circle cx="47" cy="64" r="1"/><circle cx="133" cy="64" r="1"/><circle cx="219" cy="64" r="1"/></g>
    <g stroke="var(--dk)" stroke-width=".6"><line x1="90" y1="85" x2="90" y2="96"/><line x1="176" y1="85" x2="176" y2="96"/></g>
    <g fill="var(--dk)"><circle cx="90" cy="96" r="1"/><circle cx="176" cy="96" r="1"/></g>
  </svg>
  <div class="a" style="left:27px;top:42px;width:40px;text-align:center"><div class="st">Your Title</div><div class="txt">Refers to a good or service being offered</div></div>
  <div class="a" style="left:113px;top:42px;width:40px;text-align:center"><div class="st">Your Title</div><div class="txt">Refers to a good or service being offered</div></div>
  <div class="a" style="left:199px;top:42px;width:40px;text-align:center"><div class="st">Your Title</div><div class="txt">Refers to a good or service being offered</div></div>
  <div class="a" style="left:70px;top:106px;width:40px;text-align:center"><div class="st">Your Title</div><div class="txt">Refers to a good or service being offered</div></div>
  <div class="a" style="left:156px;top:106px;width:40px;text-align:center"><div class="st">Your Title</div><div class="txt">Refers to a good or service being offered</div></div>
  <div class="folio"><span>13</span></div>
</section>

<!-- 14 puzzle circle -->
<section class="slide" style="left:326px;top:688px">
  <div class="title">Text Added Here</div><div class="logo">ROADLINE</div>
  <svg class="a" style="left:0;top:0" width="267" height="150" viewBox="0 0 267 150" font-family="Montserrat,sans-serif">
    <path d="M134 45 A25 25 0 0 0 109 70 L120 70 A14 14 0 0 1 134 56Z" fill="var(--or)"/>
    <path d="M135 45 A25 25 0 0 1 160 70 L149 70 A14 14 0 0 0 135 56Z" fill="var(--dk)"/>
    <path d="M109 71 A25 25 0 0 0 134 96 L134 85 A14 14 0 0 1 120 71Z" fill="var(--dk)"/>
    <path d="M160 71 A25 25 0 0 1 135 96 L135 85 A14 14 0 0 0 149 71Z" fill="var(--or)"/>
    <g fill="#fff"><circle cx="134.5" cy="50" r="2"/><circle cx="114" cy="70.5" r="2"/><circle cx="155" cy="70.5" r="2"/><circle cx="134.5" cy="91" r="2"/></g>
    <text x="134.5" y="70" font-size="5.2" font-weight="700" text-anchor="middle" fill="var(--dk)">Text</text>
    <text x="134.5" y="76" font-size="5.2" font-weight="700" text-anchor="middle" fill="var(--dk)">Added</text>
  </svg>
  <div class="a" style="left:25px;top:39px;width:60px;text-align:right"><div class="st" style="font-size:3.6px">Text Here</div><div class="txt">Lorem ipsum dolor sit amet, consectetuer adipiscing elit, sed diammy nibh euismod tincidunt ut laoreet dolore</div></div>
  <div class="a" style="left:25px;top:92px;width:60px;text-align:right"><div class="st" style="font-size:3.6px">Text Here</div><div class="txt">Lorem ipsum dolor sit amet, consectetuer adipiscing elit, sed diammy nibh euismod tincidunt ut laoreet dolore</div></div>
  <div class="a" style="left:179px;top:39px;width:60px"><div class="st" style="font-size:3.6px">Text Here</div><div class="txt">Lorem ipsum dolor sit amet, consectetuer adipiscing elit, sed diammy nibh euismod tincidunt ut laoreet dolore</div></div>
  <div class="a" style="left:179px;top:92px;width:60px"><div class="st" style="font-size:3.6px">Text Here</div><div class="txt">Lorem ipsum dolor sit amet, consectetuer adipiscing elit, sed diammy nibh euismod tincidunt ut laoreet dolore</div></div>
  <div class="folio"><span>14</span></div>
</section>

<!-- 15 values -->
<section class="slide" style="left:604px;top:688px">
  <div class="title">Text Added Here</div><div class="logo">ROADLINE</div>
  <div class="a" style="left:20px;top:48px;font-weight:800;font-size:12.5px;line-height:1.65"><span class="or">Lorem Ipsum<br>Dolor Sit</span><br>Ametkeeper.</div>
  <div class="a" style="left:117px;top:30px;width:12px;height:12px;background:var(--or)"></div>
  <div class="a" style="left:117px;top:64px;width:12px;height:12px;background:var(--or)"></div>
  <div class="a" style="left:117px;top:100px;width:12px;height:12px;background:var(--or)"></div>
  <div class="a" style="left:144px;top:31px;width:100px"><div class="st" style="font-size:3.8px">We Before Me</div><div class="txt" style="margin-top:1.5px">ipsum dolor sit amet, cons ectetuer adipiscing elit, sed diam nonummy nibh euismod tincidunt ut laoreet</div></div>
  <div class="a" style="left:144px;top:65px;width:100px"><div class="st" style="font-size:3.8px">We Are Good People</div><div class="txt" style="margin-top:1.5px">ipsum dolor sit amet, cons ectetuer adipiscing elit, sed diam nonummy nibh euismod tincidunt ut laoreet dolore magna aliquam erat volutpat.</div></div>
  <div class="a" style="left:144px;top:101px;width:100px"><div class="st" style="font-size:3.8px">We Work with Heart</div><div class="txt" style="margin-top:1.5px">ipsum dolor sit amet, cons ectetuer adipiscing elit, sed diam nonummy nibh euismod tincidunt.</div></div>
  <div class="folio"><span>15</span></div>
</section>

<!-- 16 cycle -->
<section class="slide" style="left:48px;top:848px">
  <div class="title">Text Added Here</div><div class="logo">ROADLINE</div>
  <div class="a txt" style="left:12px;top:27px;width:62px;font-size:2.6px">Lorem ipsum dolor sit amet, consectetuer adipiscing elit, sed diam nonummy nibh .<br><br>Ut wisi enim ad minim veniam, quis nostrud exerci tation ullamcorper suscipit lobortis.</div>
  <div class="dot" style="left:17px;top:74px;width:3px;height:3px"></div><div class="a" style="left:24px;top:72px;width:50px"><div class="st or" style="font-size:3px">Lorem ipsum</div><div class="txt" style="font-size:1.8px">Lorem ipsum dolor sit amet, consectetuer adipiscing elit, sed diam nonummy nibh euismod tincidunt</div></div>
  <div class="dot" style="left:17px;top:94px;width:3px;height:3px"></div><div class="a" style="left:24px;top:92px;width:50px"><div class="st or" style="font-size:3px">Lorem ipsum</div><div class="txt" style="font-size:1.8px">Lorem ipsum dolor sit amet, consectetuer adipiscing elit, sed diam nonummy nibh euismod tincidunt</div></div>
  <div class="dot" style="left:17px;top:115px;width:3px;height:3px"></div><div class="a" style="left:24px;top:113px;width:50px"><div class="st or" style="font-size:3px">Lorem ipsum</div><div class="txt" style="font-size:1.8px">Lorem ipsum dolor sit amet, consectetuer adipiscing elit, sed diam nonummy nibh euismod tincidunt</div></div>
  <svg class="a" style="left:0;top:0" width="267" height="150" viewBox="0 0 267 150" font-family="Montserrat,sans-serif">
    <path d="M110 92 A37 37 0 1 1 148 126" fill="none" stroke="var(--dk)" stroke-width="2.4"/>
    <path d="M106 88 L110 96 L114 88" fill="none" stroke="var(--dk)" stroke-width="1.6"/>
    <circle cx="197" cy="47" r="13" fill="#fff" stroke="var(--dk)" stroke-width="1.2"/><circle cx="197" cy="47" r="9" fill="none" stroke="var(--or)" stroke-width="4" stroke-dasharray="48 10"/>
    <circle cx="205" cy="92" r="9" fill="#fff" stroke="var(--dk)" stroke-width="1.2"/><circle cx="205" cy="92" r="6" fill="none" stroke="var(--or)" stroke-width="3" stroke-dasharray="30 8"/>
    <circle cx="183" cy="118" r="7" fill="#fff" stroke="var(--dk)" stroke-width="1.2"/><circle cx="183" cy="118" r="4.5" fill="none" stroke="var(--or)" stroke-width="2.4" stroke-dasharray="21 7"/>
    <circle cx="129" cy="111" r="6" fill="#fff" stroke="var(--dk)" stroke-width="1.2"/><circle cx="129" cy="111" r="3.8" fill="var(--or)"/>
    <g fill="var(--dk)"><rect x="143" y="65" width="2" height="8"/><rect x="146" y="68" width="2" height="5"/><rect x="149" y="66" width="2" height="7"/><rect x="152" y="69" width="2" height="4"/></g>
    <g font-size="2.8" font-weight="700" fill="var(--or)" font-style="italic"><text x="216" y="39">85%</text><text x="178" y="83">80%</text><text x="146" y="110">50%</text><text x="198" y="132">75%</text></g>
    <text x="148" y="79" font-size="3.8" font-weight="700" text-anchor="middle" fill="var(--dk)">MAIN TITLE</text>
  </svg>
  <div class="a" style="left:218px;top:44px;width:36px;text-align:right"><div class="st" style="font-size:2.8px">Your Title</div><div class="txt" style="font-size:1.6px">Lorem ipsum dolor sit amet, consectetuer adipiscing elit, sed diam nonummy nibh euismod</div></div>
  <div class="a" style="left:218px;top:82px;width:36px;text-align:right"><div class="st" style="font-size:2.8px">Your Title</div><div class="txt" style="font-size:1.6px">Lorem ipsum dolor sit amet, consectetuer adipiscing elit, sed diam nonummy nibh euismod</div></div>
  <div class="a" style="left:211px;top:113px;width:36px;text-align:right"><div class="st" style="font-size:2.8px">Your Title</div><div class="txt" style="font-size:1.6px">Lorem ipsum dolor sit amet, consectetuer adipiscing elit, sed diam nonummy nibh euismod</div></div>
  <div class="a" style="left:85px;top:104px;width:36px;text-align:right"><div class="st" style="font-size:2.8px">Your Title</div><div class="txt" style="font-size:1.6px">Lorem ipsum dolor sit amet, consectetuer adipiscing elit, sed diam nonummy nibh euismod</div></div>
  <div class="folio"><span>16</span></div>
</section>

<!-- 17 six icons -->
<section class="slide" style="left:326px;top:848px">
  <div class="title">Text Added Here</div><div class="logo">ROADLINE</div>
  <div class="a" style="left:46px;top:31px;width:20px;height:20px;background:var(--or)"></div>
  <div class="a" style="left:122px;top:31px;width:20px;height:20px;background:var(--dk)"></div>
  <div class="a" style="left:198px;top:31px;width:20px;height:20px;background:var(--or)"></div>
  <div class="a" style="left:46px;top:85px;width:20px;height:20px;background:var(--dk)"></div>
  <div class="a" style="left:122px;top:85px;width:20px;height:20px;background:var(--or)"></div>
  <div class="a" style="left:198px;top:85px;width:20px;height:20px;background:var(--dk)"></div>
  <div class="a" style="left:31px;top:56px;width:50px;text-align:center"><div class="st" style="font-size:3.4px">LOREM IPSUM</div><div class="txt" style="font-size:1.9px">Lorem ipsum dolor sit amet, consectetuer adipiscing elit, sed diam nonummy nibh euismod tincidunt ut laoreet</div></div>
  <div class="a" style="left:107px;top:56px;width:50px;text-align:center"><div class="st" style="font-size:3.4px">LOREM IPSUM</div><div class="txt" style="font-size:1.9px">Lorem ipsum dolor sit amet, consectetuer adipiscing elit, sed diam nonummy nibh euismod tincidunt ut laoreet</div></div>
  <div class="a" style="left:183px;top:56px;width:50px;text-align:center"><div class="st" style="font-size:3.4px">LOREM IPSUM</div><div class="txt" style="font-size:1.9px">Lorem ipsum dolor sit amet, consectetuer adipiscing elit, sed diam nonummy nibh euismod tincidunt ut laoreet</div></div>
  <div class="a" style="left:31px;top:110px;width:50px;text-align:center"><div class="st" style="font-size:3.4px">LOREM IPSUM</div><div class="txt" style="font-size:1.9px">Lorem ipsum dolor sit amet, consectetuer adipiscing elit, sed diam nonummy nibh euismod tincidunt ut laoreet</div></div>
  <div class="a" style="left:107px;top:110px;width:50px;text-align:center"><div class="st" style="font-size:3.4px">LOREM IPSUM</div><div class="txt" style="font-size:1.9px">Lorem ipsum dolor sit amet, consectetuer adipiscing elit, sed diam nonummy nibh euismod tincidunt ut laoreet</div></div>
  <div class="a" style="left:183px;top:110px;width:50px;text-align:center"><div class="st" style="font-size:3.4px">LOREM IPSUM</div><div class="txt" style="font-size:1.9px">Lorem ipsum dolor sit amet, consectetuer adipiscing elit, sed diam nonummy nibh euismod tincidunt ut laoreet</div></div>
  <div class="folio"><span>17</span></div>
</section>

<!-- 18 steps -->
<section class="slide" style="left:604px;top:848px">
  <div class="title">Text Added Here</div><div class="logo">ROADLINE</div>
  <svg class="a" style="left:0;top:0" width="267" height="150" viewBox="0 0 267 150" font-family="Montserrat,sans-serif">
    <rect x="20" y="70" width="100" height="4" fill="var(--or)"/><rect x="120" y="70" width="124" height="4" fill="var(--dk)"/><path d="M243 67.5 L250 72 L243 76.5Z" fill="var(--dk)"/>
    <path d="M52 71 A14 14 0 1 1 72 71" fill="none" stroke="var(--or)" stroke-width="4"/>
    <path d="M99 71 A14 14 0 1 1 119 71" fill="none" stroke="var(--dk)" stroke-width="4"/>
    <path d="M146 71 A14 14 0 1 1 166 71" fill="none" stroke="var(--or)" stroke-width="4"/>
    <path d="M193 71 A14 14 0 1 1 213 71" fill="none" stroke="var(--dk)" stroke-width="4"/>
    <g fill="none" stroke="var(--dk)" stroke-width=".7"><circle cx="62" cy="61" r="5"/><circle cx="109" cy="61" r="5"/><circle cx="156" cy="61" r="5"/><circle cx="203" cy="61" r="5"/></g>
    <g fill="#fff" font-size="2.6" font-weight="700" text-anchor="middle"><text x="70" y="73">Step 01</text><text x="117" y="73">Step 02</text><text x="164" y="73">Step 03</text><text x="221" y="73">Step 04</text></g>
    <g stroke="var(--dk)" stroke-width=".5"><line x1="62" y1="77" x2="62" y2="85"/><line x1="109" y1="77" x2="109" y2="85"/><line x1="156" y1="77" x2="156" y2="85"/><line x1="203" y1="77" x2="203" y2="85"/></g>
  </svg>
  <div class="a" style="left:44px;top:87px;width:36px;text-align:center"><div class="st" style="font-size:3.6px">Lorem Ipsum</div><div class="txt" style="font-size:1.8px">Lorem ipsum dolor sit amet, consectetuer adipiscing elit, sed diam nonummy nibh euismod tincidunt ut laoreet dolore magna aliquam erat volutpat. Ut wisi</div></div>
  <div class="a" style="left:91px;top:87px;width:36px;text-align:center"><div class="st" style="font-size:3.6px">Lorem Ipsum</div><div class="txt" style="font-size:1.8px">Lorem ipsum dolor sit amet, consectetuer adipiscing elit, sed diam nonummy nibh euismod tincidunt ut laoreet dolore magna aliquam erat volutpat. Ut wisi</div></div>
  <div class="a" style="left:138px;top:87px;width:36px;text-align:center"><div class="st" style="font-size:3.6px">Lorem Ipsum</div><div class="txt" style="font-size:1.8px">Lorem ipsum dolor sit amet, consectetuer adipiscing elit, sed diam nonummy nibh euismod tincidunt ut laoreet dolore magna aliquam erat volutpat. Ut wisi</div></div>
  <div class="a" style="left:185px;top:87px;width:36px;text-align:center"><div class="st" style="font-size:3.6px">Lorem Ipsum</div><div class="txt" style="font-size:1.8px">Lorem ipsum dolor sit amet, consectetuer adipiscing elit, sed diam nonummy nibh euismod tincidunt ut laoreet dolore magna aliquam erat volutpat. Ut wisi</div></div>
  <div class="folio"><span>18</span></div>
</section>

<!-- 19 phones -->
<section class="slide" style="left:48px;top:1008px">
  <div class="title">Text Added Here</div><div class="logo">ROADLINE</div>
  <div class="a txt" style="left:14px;top:29px;width:85px;font-size:2.3px">Lorem ipsum dolor sit amet, consectetuer adipiscing elit, sed diam nonummy nibh euismod tincidunt ut laoreet dolore magna aliquam erat volutpat. Ut wisi enim ad minim veniam,<br><br>quis nostrud exerci tation ullamcorper suscipit lobortis nisl ut aliquip ex ea commodo consequat. Duis autem vel eum iriure dolor in hendrerit in vulputate velit esse</div>
  <div class="a" style="left:23px;top:80px;width:8px;height:8px;background:var(--or);color:#fff;font-size:4px;font-weight:700;text-align:center;line-height:8px">1</div>
  <div class="a" style="left:23px;top:99px;width:8px;height:8px;background:var(--or);color:#fff;font-size:4px;font-weight:700;text-align:center;line-height:8px">2</div>
  <div class="a" style="left:23px;top:117px;width:8px;height:8px;background:var(--or);color:#fff;font-size:4px;font-weight:700;text-align:center;line-height:8px">3</div>
  <div class="a" style="left:34px;top:80px;width:70px"><div class="st" style="font-size:3px">Lorem ipsum</div><div class="txt" style="font-size:1.8px">Lorem ipsum dolor sit amet, consectetuer adipiscing elit, sed diam nonummy nibh euismod tincid</div></div>
  <div class="a" style="left:34px;top:99px;width:70px"><div class="st" style="font-size:3px">Lorem ipsum</div><div class="txt" style="font-size:1.8px">Lorem ipsum dolor sit amet, consectetuer adipiscing elit, sed diam nonummy nibh euismod tincid</div></div>
  <div class="a" style="left:34px;top:117px;width:70px"><div class="st" style="font-size:3px">Lorem ipsum</div><div class="txt" style="font-size:1.8px">Lorem ipsum dolor sit amet, consectetuer adipiscing elit, sed diam nonummy nibh euismod tincid</div></div>
  <svg class="a" style="left:0;top:0" width="267" height="150" viewBox="0 0 267 150" font-family="Montserrat,sans-serif">
    <g fill="#fff" stroke="var(--dk)" stroke-width="1"><rect x="123" y="24" width="31" height="64" rx="3"/><rect x="163" y="44" width="31" height="64" rx="3"/><rect x="202" y="64" width="31" height="64" rx="3"/></g>
    <g fill="var(--dk)"><rect x="134" y="25" width="9" height="1.6" rx=".8"/><rect x="174" y="45" width="9" height="1.6" rx=".8"/><rect x="213" y="65" width="9" height="1.6" rx=".8"/></g>
    <g fill="none" stroke="var(--or)" stroke-width=".6"><rect x="134" y="48" width="8" height="6"/><rect x="174" y="67" width="8" height="7"/><circle cx="218" cy="90" r="4"/></g>
    <g fill="var(--dk)" font-size="3.4"><text x="126" y="34">Lorem</text><text x="126" y="38.5">ipsum dolor</text><text x="166" y="54">Dolor sit</text><text x="166" y="58.5">amet, conse</text><text x="205" y="75">Consec</text></g>
  </svg>
  <div class="a txt" style="left:126px;top:57px;width:25px;font-size:1.4px">To introduce the students to the changing landscape of marketing strategies with a focus on the digital world.</div>
  <div class="a txt" style="left:166px;top:77px;width:25px;font-size:1.4px">You will learn concepts and ideas in digital marketing as well as the tools and strategies to optimise campaigns.</div>
  <div class="a txt" style="left:205px;top:97px;width:25px;font-size:1.4px">You are required to score 80% or the evaluation test to obtain the certificate. Retry up to three times.</div>
  <div class="folio"><span>19</span></div>
</section>

<!-- 20 team -->
<section class="slide" style="left:326px;top:1008px">
  <div class="title">Text Added Here</div><div class="logo">ROADLINE</div>
  <div class="a" style="left:24px;top:47px;width:39px;height:15px;background:var(--dk)"></div>
  <div class="a" style="left:85px;top:47px;width:39px;height:15px;background:var(--or)"></div>
  <div class="a" style="left:145px;top:47px;width:39px;height:15px;background:var(--dk)"></div>
  <div class="a" style="left:206px;top:47px;width:39px;height:15px;background:var(--or)"></div>
  <div class="ph" role="img" aria-label="Portrait photo of team member" style="left:33px;top:50px;width:21px;height:21px;border-radius:50%;background:linear-gradient(#ddd,#aaa);border:1px solid #fff"></div>
  <div class="ph" role="img" aria-label="Portrait photo of team member" style="left:94px;top:50px;width:21px;height:21px;border-radius:50%;background:linear-gradient(#ddd,#aaa);border:1px solid #fff"></div>
  <div class="ph" role="img" aria-label="Portrait photo of team member" style="left:154px;top:50px;width:21px;height:21px;border-radius:50%;background:linear-gradient(#ddd,#aaa);border:1px solid #fff"></div>
  <div class="ph" role="img" aria-label="Portrait photo of team member" style="left:215px;top:50px;width:21px;height:21px;border-radius:50%;background:linear-gradient(#ddd,#aaa);border:1px solid #fff"></div>
  <div class="a" style="left:18px;top:75px;width:51px;text-align:center"><div class="st or" style="font-size:3.8px">ARON VALE</div><div class="txt" style="font-size:1.8px;margin-top:1px">Lorem ipsum dolor sit amet, cons ectetuer adipiscing elit, sed diam nonummy nibh euismod tincidunt<br><br>ut laoreet dolore magna aliquam erat volutpat. Ut wisi enim ad minim veniam, quis nostrud</div></div>
  <div class="a" style="left:79px;top:75px;width:51px;text-align:center"><div class="st" style="font-size:3.8px">NINA HOLLIS</div><div class="txt" style="font-size:1.8px;margin-top:1px">Lorem ipsum dolor sit amet, cons ectetuer adipiscing elit, sed diam nonummy nibh euismod tincidunt<br><br>ut laoreet dolore magna aliquam erat volutpat. Ut wisi enim ad minim veniam, quis nostrud</div></div>
  <div class="a" style="left:139px;top:75px;width:51px;text-align:center"><div class="st or" style="font-size:3.8px">ARON VALE</div><div class="txt" style="font-size:1.8px;margin-top:1px">Lorem ipsum dolor sit amet, cons ectetuer adipiscing elit, sed diam nonummy nibh euismod tincidunt<br><br>ut laoreet dolore magna aliquam erat volutpat. Ut wisi enim ad minim veniam, quis nostrud</div></div>
  <div class="a" style="left:200px;top:75px;width:51px;text-align:center"><div class="st" style="font-size:3.8px">NINA HOLLIS</div><div class="txt" style="font-size:1.8px;margin-top:1px">Lorem ipsum dolor sit amet, cons ectetuer adipiscing elit, sed diam nonummy nibh euismod tincidunt<br><br>ut laoreet dolore magna aliquam erat volutpat. Ut wisi enim ad minim veniam, quis nostrud</div></div>
  <div class="folio"><span>20</span></div>
</section>

<!-- 21 thank you -->
<section class="slide" style="left:604px;top:1008px">
  <div class="a" style="left:31px;top:66px;font-weight:800;font-size:15px">ROADLINE</div>
  <div class="a" style="left:145px;top:36px;font-weight:800;font-size:15px">Thank You</div>
  <svg class="a" style="left:145px;top:68px" width="10" height="60" viewBox="0 0 10 60">
    <path d="M1.5 1.5 C1.5 6 4 8.5 8 8.5 L8 6.5 L6 6 L5 7 C4 6.5 3 5.5 2.8 4.5 L3.8 3.5 L3.2 1.5Z" fill="var(--or)"/>
    <path d="M1 21 L8 18 L5 25 L4.2 22Z" fill="var(--or)"/>
    <path d="M1 42 L4.5 38.5 L8 42 L7 42 L7 45 L2 45 L2 42Z" fill="var(--or)"/>
    <g stroke="var(--dk)" stroke-width=".5"><line x1="9.5" y1="1" x2="9.5" y2="9"/><line x1="9.5" y1="18" x2="9.5" y2="26"/><line x1="9.5" y1="38" x2="9.5" y2="46"/></g>
  </svg>
  <div class="a txt" style="left:162px;top:68px;font-size:3.2px;color:#555;line-height:1.35">+18 5550 1200 3400<br>+18 5550 1200 3400</div>
  <div class="a txt" style="left:162px;top:85px;font-size:3.2px;color:#555;line-height:1.35">www.roadline-freight.com<br>hello@roadline-freight.com</div>
  <div class="a txt" style="left:162px;top:105px;width:90px;font-size:3.2px;color:#555;line-height:1.35">88 Depot Lane, Fairhaven,<br>State 40210</div>
</section>

</main>
</body>
</html>
```